Banner Designs for Drone Defense Ad Campaign

Corvane is a security consulting and services company that offers a service called SkyMindful. SkyMindful helps our customers identify security risks from drones and develops comprehensive protection programs. We are looking for a designer to create a banner ad in three sizes for our campaign.
Target Market(s)
Our campaign is geared to the sports and entertainment industry, specifically large event venues and their security operation.
Industry/Entity Type
Security
Font styles to use
Other font styles liked:
- Raleway
Requirements
Must have
- Banner Objective
The visual and textual content of the banner should prompt the viewer to quickly identify the service offered and the information that is available to download.
Banner Design
Logo: SkyMindful logo
Call to Action Button in Red: Get It Here (On Right or or Upper Right)
Title in Larger Font: Guide to UAS Risk Mitigation
Subtitle in smaller Font: 5 Steps to Develop Your Comprehensive UAS Defense Program
Background: Stadium with a drone flying in foreground
Font: Raleway
Banner Sizes
1 - 1200x670 pixels
2 - 1510x196 pixels
3 - 1200x628 pixels

```html
<!DOCTYPE html>
<html lang="en">
<head>
<meta charset="utf-8">
<title>SkyMindful – Guide to UAS Risk Mitigation</title>
<link href="https://fonts.googleapis.com/css2?family=Raleway:wght@400;500;600&display=swap" rel="stylesheet">
<style>
  :root {
    --bg-top: #1b1b1b;
    --bg-bottom: #101010;
    --venue-tone: #2b2b2b;
    --panel: #262829;
    --target-red: #ff0000;
    --track-green: #39d63c;
    --alert-yellow: #f2d21b;
    --title-blue: #3778bd;
    --brand-blue: #6f8fb3;
    --text-white: #ffffff;
    --text-grey: #d8d8d8;
    --cta-red: #f40000;
  }
  * { margin: 0; padding: 0; box-sizing: border-box; }
  html, body { width: 1200px; height: 670px; overflow: hidden; background: var(--bg-bottom); }
  .banner {
    position: relative;
    width: 1200px;
    height: 670px;
    overflow: hidden;
    font-family: "Raleway", sans-serif;
    background: linear-gradient(180deg, var(--bg-top) 0%, var(--bg-bottom) 100%);
  }
  .venue-backdrop {
    position: absolute;
    left: 0; top: 240px;
    width: 1200px; height: 430px;
    background: radial-gradient(ellipse 520px 260px at 800px 250px, var(--venue-tone) 0%, rgba(30,30,30,0.6) 55%, rgba(16,16,16,0) 100%);
  }
  .tracking-frame {
    position: absolute;
    left: 62px; top: 58px;
    width: 268px; height: 182px;
    background: var(--panel);
  }
  .drone-figure {
    position: absolute;
    left: 24px; top: 22px;
    width: 240px; height: 140px;
    background: radial-gradient(ellipse 110px 60px at 110px 65px, rgba(57,214,60,0.55) 0%, rgba(57,214,60,0.15) 60%, rgba(57,214,60,0) 100%);
  }
  .frame-corners { position: absolute; left: 0; top: 0; }
  .tracker-line {
    position: absolute;
    left: 133px; top: 240px;
    width: 2px; height: 182px;
    background: var(--track-green);
  }
  .readout {
    position: absolute;
    left: 148px; top: 290px;
    font-size: 16px;
    line-height: 21.5px;
    color: var(--track-green);
  }
  .readout .status { color: var(--alert-yellow); font-weight: 500; }
  .readout .model { font-weight: 600; font-size: 17px; }
  .brand {
    position: absolute;
    right: 56px; top: 78px;
    text-align: right;
  }
  .brand-name {
    display: inline-flex;
    align-items: center;
    gap: 10px;
    font-size: 30px;
    font-weight: 500;
    color: var(--brand-blue);
    line-height: 1;
  }
  .brand-dot { width: 12px; height: 12px; border-radius: 50%; background: var(--brand-blue); }
  .brand-byline { font-size: 17px; color: var(--text-grey); margin-top: 6px; padding-right: 10px; }
  .headline {
    position: absolute;
    right: 48px; top: 188px;
    text-align: right;
    color: var(--title-blue);
    font-weight: 400;
    font-size: 72px;
    line-height: 88px;
    letter-spacing: 0.5px;
  }
  .subhead {
    position: absolute;
    right: 48px; top: 372px;
    text-align: right;
    color: var(--text-white);
    font-size: 27px;
    line-height: 42px;
    font-weight: 400;
  }
  .cta-button {
    position: absolute;
    left: 760px; top: 488px;
    width: 396px; height: 92px;
    background: var(--cta-red);
    color: var(--text-white);
    font-size: 46px;
    font-weight: 500;
    display: flex; align-items: center; justify-content: center;
    text-decoration: none;
  }
</style>
</head>
<body>
<div class="banner">
  <div class="venue-backdrop" role="img" aria-label="Dimly lit stadium exterior at dusk with light poles"></div>

  <div class="tracking-frame">
    <div class="drone-figure" role="img" aria-label="Green silhouette of a quadcopter drone"></div>
    <svg class="frame-corners" width="268" height="182" viewBox="0 0 268 182">
      <g fill="none" stroke="var(--target-red)" stroke-width="7">
        <path d="M3.5 40 V3.5 H40"/>
        <path d="M228 3.5 H264.5 V40"/>
        <path d="M3.5 142 V178.5 H40"/>
        <path d="M228 178.5 H264.5 V142"/>
      </g>
    </svg>
  </div>
  <div class="tracker-line"></div>

  <div class="readout">
    <div class="status">DRONE TRACKED!</div>
    <div class="model">Vexa Hover</div>
    <div>Loc :&nbsp; -6°13'4.12" S 106°48'5.41" E</div>
    <div>Height : 112 feet</div>
    <div>Distance : 215 feet</div>
    <div>Speed : 30 mph</div>
  </div>

  <div class="brand">
    <div class="brand-name"><span class="brand-dot"></span>SkyMindful</div>
    <div class="brand-byline">By Corvane</div>
  </div>

  <h1 class="headline">Guide to<br>UAS Risk Mitigation</h1>
  <p class="subhead">5 Steps to Develop Your Comprehensive<br>UAS Defense Program</p>

  <a class="cta-button" href="#">Get It Here</a>
</div>
</body>
</html>
```